A new art and beauty business needing a eCommerce design

I need an ecommerce design for my company that is based in Australia called 'Fern and Fable'. I make art and other products and would like the website to be an easy to use website, it must however, look modern and professional.

Could you please provide the finished product CODED with HTML etc. and ready to be used.

Colours can be chosen by the designer and are not limited in any way by our previous websites design.

I look forward to your submissions and will reward good work with our approval for payment.

If you would like further information you are welcome to ask.

Industry/Entity Type

Business

Contact Information for Business Card

Company Name: Fern and Fable

Owners Name: Darren Vollmacht

Address: 14 Copperfield Row
Tumbarra, NSW 2687
Australia

Phone: 0491 786 215

Email: contact@fern-andfable.com

Logo Text

Fern and Fable

```html
<!DOCTYPE html>
<html lang="en">
<head>
<meta charset="utf-8">
<title>Fern and Fable</title>
<link href="https://fonts.googleapis.com/css2?family=Open+Sans:wght@400;600;700&family=Dancing+Script:wght@700&display=swap" rel="stylesheet">
<style>
:root{
  --pink:#e8308a;
  --pink-dark:#c91f72;
  --nav:#3f3f3f;
  --page:#f2f2f2;
  --panel:#ffffff;
  --line:#dcdcdc;
  --text:#555555;
  --muted:#8a8a8a;
  --footer:#e6e6e6;
  --bottom:#3a3a3a;
}
*{box-sizing:border-box;margin:0;padding:0}
html,body{width:745px;height:1200px;overflow:hidden}
body{background:var(--page);font-family:"Open Sans",Arial,sans-serif;color:var(--text);font-size:9px;position:relative}
.wrap{width:635px;margin:0 auto;position:relative}

.topbar{height:22px;background:#fafafa;border-bottom:1px solid var(--line)}
.topbar .wrap{display:flex;justify-content:space-between;align-items:center;height:22px;font-size:7px;color:var(--muted)}

.header{height:58px;background:#fff}
.header .wrap{display:flex;align-items:center;justify-content:space-between;height:58px}
.brand{display:flex;align-items:center;gap:8px}
.brand-dot{width:30px;height:30px;border-radius:50%;background:var(--pink)}
.brand-name{font-size:17px;font-weight:600;color:#777}
.tools{display:flex;align-items:center;gap:10px}
.search{display:flex;border:1px solid var(--line)}
.search span{width:105px;height:20px;font-size:7px;color:#aaa;padding:5px 6px}
.search button{width:20px;height:20px;border:0;background:var(--pink);display:flex;align-items:center;justify-content:center}
.cart{width:22px;height:22px;border-radius:50%;border:1px solid var(--line);position:relative;display:flex;align-items:center;justify-content:center}
.cart b{position:absolute;top:-6px;right:-5px;width:11px;height:11px;border-radius:50%;background:var(--pink);color:#fff;font-size:6px;text-align:center;line-height:11px}

.nav{height:32px;background:var(--nav);display:flex}
.nav a{color:#eee;text-decoration:none;font-size:8px;font-weight:600;padding:0 13px;line-height:32px}
.nav a.active{background:var(--pink)}

.hero{margin-top:13px;height:315px;background:linear-gradient(100deg,#fff 0%,#fdf6fa 40%,#f3f7fd 100%);position:relative;border:1px solid var(--line)}
.hero-copy{position:absolute;left:30px;top:95px}
.hero-copy h2{font-size:14px;font-weight:600;color:#555;letter-spacing:.3px}
.hero-copy .save{font-size:34px;font-weight:700;color:var(--pink);line-height:1.2}
.hero-copy p{font-size:12px;color:#666;font-weight:600}
.arrows{display:flex;gap:3px;margin-top:18px}
.arrow{width:14px;height:18px;background:#444;display:flex;align-items:center;justify-content:center}
.hero-art{position:absolute;left:300px;top:25px;width:320px;height:265px;background:linear-gradient(120deg,#ff4d8d,#ffd23f 35%,#3ec7f2 65%,#8d4de8);box-shadow:0 4px 10px rgba(0,0,0,.25);transform:rotate(-3deg)}

.promos{display:flex;gap:12px;margin-top:25px}
.promo{flex:1;height:145px;background:var(--panel);border:1px solid var(--line);position:relative;padding:28px 0 0 16px}
.promo h3{font-family:"Dancing Script",cursive;font-size:24px;color:var(--pink);line-height:1}
.promo h4{font-size:12px;color:#666;font-weight:600}
.promo p{font-size:6px;color:var(--muted);margin:3px 0 10px}
.btn{display:inline-block;background:var(--pink);color:#fff;font-size:7px;font-weight:700;padding:5px 10px;border-radius:2px}
.promo-img{position:absolute;right:14px;top:22px;width:130px;height:100px}

.featured-head{margin-top:18px;display:flex;justify-content:space-between;align-items:center;height:20px}
.featured-head h3{font-size:11px;font-weight:700;color:#444}
.featured-head h3 span{color:var(--pink)}
.pager{display:flex;gap:3px}
.pager i{width:13px;height:13px;border-radius:50%;background:#444;display:flex;align-items:center;justify-content:center}

.products{display:flex;gap:14px;margin-top:8px}
.card{flex:1;height:200px;background:var(--panel);border:1px solid var(--line);padding:8px;position:relative}
.card .img{height:135px}
.card h5{font-size:8px;color:#444;font-weight:600;margin-top:9px}
.card .price{font-size:7px;color:var(--muted);margin-top:3px}
.card .add{position:absolute;right:10px;bottom:22px;width:18px;height:18px;border-radius:50%;background:var(--pink);display:flex;align-items:center;justify-content:center}

.gift{margin-top:12px;height:113px;position:relative;border:1px solid var(--line);background:linear-gradient(90deg,#f6d84a,#fdf3c8 30%,#fbe7f1 60%,#cdeaf9 85%,#9fd8f6);text-align:center;padding-top:62px}
.gift p{font-size:7px;color:#333}
.gift .btn{margin-top:6px;padding:5px 14px;font-size:8px}

.footer{position:absolute;left:0;top:995px;width:745px;height:155px;background:var(--footer)}
.footer .wrap{display:flex;padding-top:14px}
.col h6{font-size:8px;color:var(--pink);font-weight:700;margin-bottom:7px}
.col p,.col li{font-size:6.5px;color:#777;line-height:1.6;list-style:none}
.col-contact{width:190px}
.col-account{width:140px}
.col-news{width:140px}
.field{display:flex;margin:6px 0 10px;width:115px}
.field span{flex:1;height:14px;background:#fff;border:1px solid var(--line)}
.field i{width:14px;height:14px;background:var(--pink)}
.cards-row{display:flex;gap:4px;margin-top:4px}
.cards-row i{width:18px;height:12px;background:#fff;border:1px solid #ccc}
.col-brand .brand-name{font-size:10px}
.col-brand .brand-dot{width:16px;height:16px}
.col-brand .brand{gap:5px;margin-bottom:8px}
.thumbs{display:grid;grid-template-columns:repeat(3,34px);gap:3px}
.thumbs i{height:28px}

.bottom{position:absolute;left:0;top:1150px;width:745px;height:50px;background:var(--bottom)}
.bottom .wrap{display:flex;justify-content:space-between;align-items:center;height:50px;color:#bbb;font-size:7px}
.social{display:flex;gap:4px}
.social i{width:14px;height:14px;background:#5a5a5a}
.social i.up{background:var(--pink)}
</style>
</head>
<body>
<div class="topbar"><div class="wrap"><span>CALL FREE : 0000 00 123</span><span>REGISTER &nbsp;|&nbsp; SIGN IN</span></div></div>

<header class="header"><div class="wrap">
  <div class="brand"><span class="brand-dot"></span><span class="brand-name">Fern and Fable</span></div>
  <div class="tools">
    <div class="search"><span>Search</span><button aria-label="Search"><svg width="9" height="9" viewBox="0 0 10 10"><circle cx="4" cy="4" r="3" fill="none" stroke="#fff" stroke-width="1.5"/><line x1="6.2" y1="6.2" x2="9" y2="9" stroke="#fff" stroke-width="1.5"/></svg></button></div>
    <div class="cart"><svg width="11" height="10" viewBox="0 0 12 10"><path d="M1 1h2l1.5 6h6l1-4H4" fill="none" stroke="#777" stroke-width="1.2"/><circle cx="5" cy="9" r=".9" fill="#777"/><circle cx="10" cy="9" r=".9" fill="#777"/></svg><b>0</b></div>
  </div>
</div></header>

<main class="wrap">
  <nav class="nav">
    <a class="active">HOME</a><a>SHOP</a><a>PRODUCT</a><a>BLOG</a><a>SHOPPING CART</a><a>CHECKOUT</a><a>ABOUT US</a><a>CONTACT US</a>
  </nav>

  <section class="hero">
    <div class="hero-copy">
      <h2>FERN AND FABLE PRODUCTS</h2>
      <div class="save">20% SAVE</div>
      <p>IPSUM IS SIMPLY DUMMY TEXT</p>
      <div class="arrows">
        <span class="arrow"><svg width="6" height="8" viewBox="0 0 6 8"><path d="M5 0L1 4l4 4" fill="none" stroke="#fff" stroke-width="1.5"/></svg></span>
        <span class="arrow"><svg width="6" height="8" viewBox="0 0 6 8"><path d="M1 0l4 4-4 4" fill="none" stroke="#fff" stroke-width="1.5"/></svg></span>
      </div>
    </div>
    <div class="hero-art" role="img" aria-label="Canvas covered in bright melted crayon colour runs"></div>
  </section>

  <section class="promos">
    <div class="promo">
      <h3>Art</h3><h4>PRODUCTS</h4><p>Lorem is simply dummy text</p><span class="btn">BUY NOW</span>
      <div class="promo-img" role="img" aria-label="Colourful paint splash artwork" style="background:linear-gradient(135deg,#ff5fa2,#ffd34d 45%,#46c3ef)"></div>
    </div>
    <div class="promo">
      <h3>Art</h3><h4>PRODUCTS</h4><p>Lorem is simply dummy text</p><span class="btn">BUY NOW</span>
      <div class="promo-img" role="img" aria-label="Two purple candles in glass jars" style="background:linear-gradient(180deg,#f4f4f4,#c9c4e6 45%,#5e4fb8)"></div>
    </div>
  </section>

  <div class="featured-head">
    <h3>FEATURED <span>PRODUCTS</span></h3>
    <div class="pager"><i><svg width="5" height="6" viewBox="0 0 5 6"><path d="M4 0L1 3l3 3" fill="none" stroke="#fff"/></svg></i><i><svg width="5" height="6" viewBox="0 0 5 6"><path d="M1 0l3 3-3 3" fill="none" stroke="#fff"/></svg></i></div>
  </div>

  <section class="products">
    <div class="card"><div class="img" role="img" aria-label="Rainbow melted crayon canvas" style="background:linear-gradient(135deg,#ff4e8e,#ffcf3d 40%,#3ec4f0 75%,#7c4de6)"></div><h5>Product Name</h5><div class="price">ONLY $20</div><span class="add"><svg width="8" height="7" viewBox="0 0 12 10"><path d="M1 1h2l1.5 6h6l1-4H4" fill="none" stroke="#fff" stroke-width="1.5"/></svg></span></div>
    <div class="card"><div class="img" role="img" aria-label="Two purple candles in glass jars" style="background:linear-gradient(180deg,#eee,#b9b3dc 45%,#5a4bb3)"></div><h5>Product Name</h5><div class="price">ONLY $20</div><span class="add"><svg width="8" height="7" viewBox="0 0 12 10"><path d="M1 1h2l1.5 6h6l1-4H4" fill="none" stroke="#fff" stroke-width="1.5"/></svg></span></div>
    <div class="card"><div class="img" role="img" aria-label="Paint splash artwork on white canvas" style="background:linear-gradient(135deg,#f7f7f7,#ffcb3f 30%,#58c7e8 60%,#ef5fa0)"></div><h5>Product Name</h5><div class="price">ONLY $20</div><span class="add"><svg width="8" height="7" viewBox="0 0 12 10"><path d="M1 1h2l1.5 6h6l1-4H4" fill="none" stroke="#fff" stroke-width="1.5"/></svg></span></div>
    <div class="card"><div class="img" role="img" aria-label="Multicolour melted crayon canvas" style="background:linear-gradient(135deg,#ffd93b,#ff6a3d 35%,#e73c8d 60%,#3b9be8)"></div><h5>Product Name</h5><div class="price">ONLY $20</div><span class="add"><svg width="8" height="7" viewBox="0 0 12 10"><path d="M1 1h2l1.5 6h6l1-4H4" fill="none" stroke="#fff" stroke-width="1.5"/></svg></span></div>
  </section>

  <section class="gift" role="img" aria-label="Paint splash banner with hand lettered art gift ideas heading">
    <p>Lorem Ipsum is simply dummy text of the printing and typesetting industry</p>
    <span class="btn">Buy Now</span>
  </section>
</main>

<footer class="footer"><div class="wrap">
  <div class="col col-contact"><h6>CONTACT US</h6><p>Lorem ipsum text is simply the<br>standard dummy text ever since<br>when an unknown printer<br>Tel: 0 000 000 000<br>contact@yourcompany.com</p></div>
  <div class="col col-account"><h6>MY ACCOUNT</h6><ul><li>Your Account</li><li>My orders</li><li>My credit slips</li><li>My addresses</li><li>Login</li></ul></div>
  <div class="col col-news"><h6>NEWSLETTER</h6><p>Sign Up For Our Newsletter</p><div class="field"><span></span><i></i></div><p>Payment</p><div class="cards-row"><i></i><i></i><i></i><i></i></div></div>
  <div class="col col-brand"><div class="brand"><span class="brand-dot"></span><span class="brand-name">Fern and Fable</span></div>
    <div class="thumbs">
      <i role="img" aria-label="Shop photo" style="background:linear-gradient(135deg,#ff6fa7,#ffd56b)"></i>
      <i role="img" aria-label="Shop photo" style="background:linear-gradient(135deg,#8fd4f2,#f0f0f0)"></i>
      <i role="img" aria-label="Shop photo" style="background:linear-gradient(135deg,#b8a9e6,#5e4fb8)"></i>
      <i role="img" aria-label="Shop photo" style="background:linear-gradient(135deg,#ffd23f,#ef5f9f)"></i>
      <i role="img" aria-label="Shop photo" style="background:linear-gradient(135deg,#d9d9d9,#9c9c9c)"></i>
      <i role="img" aria-label="Shop photo" style="background:linear-gradient(135deg,#4ec1ee,#8d4de8)"></i>
    </div>
  </div>
</div></footer>

<div class="bottom"><div class="wrap"><span>Copyright © 2014 . All rights reserved.</span><div class="social"><i></i><i></i><i></i><i></i><i class="up"></i></div></div></div>
</body>
</html>
```